Bright Path Rehabilitation Stationary
Business Card, Letter Head, Envelope, Fax Cover, Invoice & Referral/Prescription Pad
Bright Path Rehabilitation Stationary  -
Creative Brief
Use specific fonts
Please use standard or same font as in logo
Simple
Gregory Lindqvist
Marketing/Administrative Director
27415 PT Hargrove Blvd # D Palo Mesa North, AZ 85291
gregory@brightpathrehab.com
www.brightpathrehab.com
Please include on the front of the card "Comprehensive Outpatient Rehabilitation Facility".Physical Therapy and Psych/Social Services. Please draw up another business card with same information except Monica Lindqvist with a title of Physical Therapist. For the fax cover sheet, envelope, referral/prescription pad and letter head please incorporate logo. We have included a map as well for referral/prescription pads.
Hands on Approach Individualized Plan of Care Friendly, Caring Staff

```html
<!DOCTYPE html>
<html lang="en">
<head>
<meta charset="utf-8">
<title>Bright Path Rehabilitation Stationery</title>
<link href="https://fonts.googleapis.com/css2?family=Open+Sans:wght@400;600;700&display=swap" rel="stylesheet">
<style>
:root{
  --bg:#e6e4e0;
  --paper:#ffffff;
  --ink:#3a3f46;
  --muted:#8a9099;
  --rule:#c9cdd2;
  --blue:#2f7fd0;
  --blue-deep:#1f5ea8;
  --steel:#a3a9b0;
  --black:#141518;
  --band-dark:#3c4047;
  --brand:#2a6fb8;
}
*{box-sizing:border-box;margin:0;padding:0}
html,body{width:1200px;height:830px;overflow:hidden;background:var(--bg)}
body{position:relative;font-family:'Open Sans',Arial,sans-serif;color:var(--ink)}
.sheet{position:absolute;background:var(--paper);box-shadow:0 3px 10px rgba(0,0,0,.22);overflow:hidden}
.brand{font-family:'Open Sans',Arial,sans-serif;font-weight:700;color:var(--brand);display:flex;align-items:center;gap:5px;line-height:1.1;white-space:nowrap}
.brand .dot{width:7px;height:7px;border-radius:50%;background:var(--brand);flex:none}
.brand.light{color:#fff}
.brand.light .dot{background:#fff}
.footer-band{position:absolute;left:0;right:0;bottom:0;height:var(--band,24px);background:var(--steel);border-top:2px solid var(--blue);box-shadow:0 -3px 0 #fff inset}
.footer-band.dark{background:var(--band-dark)}
.tiny{font-size:6px;color:var(--muted);line-height:1.5}
.field{font-size:6px;color:var(--ink);border-bottom:1px solid var(--rule);padding:3px 0;white-space:nowrap}

/* fax */
.fax{left:204px;top:36px;width:247px;height:348px;--band:34px}
.fax .brand{position:absolute;left:14px;top:14px;font-size:11px}
.fax .label{position:absolute;right:14px;top:38px;font-size:10px;font-weight:700;color:var(--muted);letter-spacing:2px}
.fax .head{position:absolute;left:0;right:0;top:52px;height:2px;background:var(--steel)}
.fax .grid{position:absolute;left:14px;right:14px;top:62px;display:grid;grid-template-columns:1fr 1fr;column-gap:14px}
.fax .checks{position:absolute;left:14px;right:14px;top:130px;display:flex;justify-content:space-between;font-size:5.5px;color:var(--muted)}
.checks span::before{content:"";display:inline-block;width:5px;height:5px;border:1px solid var(--steel);margin-right:2px;vertical-align:-1px}

/* business cards */
.card{width:166px;height:92px;--band:14px}
.card.front .brand{position:absolute;left:10px;top:9px;font-size:8px}
.card.front .info{position:absolute;right:10px;top:9px;text-align:right;font-size:5.5px;line-height:1.45;color:var(--ink)}
.card.front .info b{font-size:6.5px;color:var(--blue-deep)}
.card.back{background:var(--black)}
.card.back .brand{position:absolute;left:0;right:0;top:26px;justify-content:center;font-size:10px}
.card.back .tag{position:absolute;left:0;right:0;top:48px;text-align:center;font-size:5px;color:#c8ccd2;letter-spacing:.4px}

/* letterhead */
.letter{left:643px;top:36px;width:245px;height:336px;--band:28px}
.letter .brand{position:absolute;left:14px;top:14px;font-size:11px}
.letter .addr{position:absolute;right:14px;top:14px;text-align:right}

/* envelopes */
.env{left:893px;width:235px;height:72px;--band:12px}
.env .brand{position:absolute;left:10px;top:9px;font-size:10px}
.env .addr{position:absolute;left:10px;top:28px}
.pocket{left:893px;top:212px;width:235px;height:160px;background:#f3f4f5;--band:28px}
.pocket .flap{position:absolute;left:0;top:60px;width:235px;height:100px}

/* invoice */
.invoice{left:204px;top:408px;width:247px;height:312px;--band:20px}
.invoice .brand{position:absolute;left:14px;top:14px;font-size:11px}
.invoice .title{position:absolute;right:14px;top:14px;font-size:10px;font-weight:700;color:var(--blue-deep);letter-spacing:1px}
.invoice .meta{position:absolute;right:14px;top:32px;width:90px}
.invoice .bill{position:absolute;left:14px;top:70px;width:110px}
.invoice table{position:absolute;left:14px;top:110px;width:219px;border-collapse:collapse;font-size:5.5px}
.invoice th{background:#7d848c;color:#fff;font-weight:600;text-align:left;padding:3px}
.invoice td{height:9px;border-bottom:1px solid var(--rule);background:#eef0f2}
.invoice .total{position:absolute;right:14px;top:258px;width:80px}

/* referral */
.referral{left:660px;top:408px;width:216px;height:312px;--band:20px}
.referral .brand{position:absolute;left:12px;top:12px;font-size:9px}
.referral .title{position:absolute;right:12px;top:12px;text-align:right;font-size:8px;font-weight:700;color:var(--ink);line-height:1.3}
.referral .fields{position:absolute;left:12px;right:12px;top:46px}
.referral .rx{position:absolute;left:12px;top:122px;font-size:14px;font-weight:700;color:var(--steel)}
.referral .map{position:absolute;left:12px;top:190px;width:110px;height:70px;background:linear-gradient(135deg,#eceef0,#d4d8dc);border:1px solid var(--rule)}
.referral .sign{position:absolute;right:12px;top:200px;width:70px}

/* brand lockup */
.lockup{position:absolute;left:930px;top:712px;width:250px;display:flex;justify-content:center}
.lockup .brand{font-size:18px;color:var(--brand)}
.lockup .brand .dot{width:12px;height:12px}
</style>
</head>
<body>

<section class="sheet fax">
  <div class="brand"><span class="dot"></span>Bright Path</div>
  <div class="label">FAX</div>
  <div class="head"></div>
  <div class="grid">
    <div class="field">To:</div><div class="field">From:</div>
    <div class="field">Fax:</div><div class="field">Pages:</div>
    <div class="field">Phone:</div><div class="field">Date:</div>
    <div class="field">Re:</div><div class="field">CC:</div>
  </div>
  <div class="checks"><span>Urgent</span><span>For Review</span><span>Please Comment</span><span>Please Reply</span></div>
  <div class="footer-band"></div>
</section>

<section class="sheet card front" style="left:463px;top:36px">
  <div class="brand"><span class="dot"></span>Bright Path</div>
  <div class="info"><b>Gregory Lindqvist</b><br>Marketing/Administrative Director<br>27415 PT Hargrove Blvd # D<br>Palo Mesa North, AZ 85291<br>gregory@brightpathrehab.com<br>www.brightpathrehab.com</div>
  <div class="footer-band"></div>
</section>
<section class="sheet card back" style="left:463px;top:132px">
  <div class="brand light"><span class="dot"></span>Bright Path</div>
  <div class="tag">Comprehensive Outpatient Rehabilitation Facility</div>
  <div class="footer-band dark"></div>
</section>
<section class="sheet card front" style="left:463px;top:236px;height:120px;--band:16px">
  <div class="brand"><span class="dot"></span>Bright Path</div>
  <div class="info" style="top:34px">Physical Therapy<br>Psych/Social Services<br>Hands on Approach<br>Individualized Plan of Care</div>
  <div class="footer-band"></div>
</section>

<section class="sheet letter">
  <div class="brand"><span class="dot"></span>Bright Path</div>
  <div class="addr tiny">27415 PT Hargrove Blvd # D<br>Palo Mesa North, AZ 85291<br>P (555) 203-0148 · F (555) 203-0149<br>www.brightpathrehab.com</div>
  <div class="footer-band"></div>
</section>

<section class="sheet env" style="top:36px">
  <div class="brand"><span class="dot"></span>Bright Path</div>
  <div class="addr tiny">27415 PT Hargrove Blvd # D<br>Palo Mesa North, AZ 85291</div>
  <div class="footer-band"></div>
</section>
<section class="sheet env" style="top:118px;height:88px;--band:14px">
  <div class="brand"><span class="dot"></span>Bright Path</div>
  <div class="addr tiny">27415 PT Hargrove Blvd # D<br>Palo Mesa North, AZ 85291</div>
  <div class="footer-band"></div>
</section>
<section class="sheet pocket">
  <svg class="flap" viewBox="0 0 235 100" aria-hidden="true"><path d="M0 10 L117 70 L235 10 V100 H0Z" fill="#e1e4e7"/><path d="M0 10 L117 70 L235 10" stroke="var(--rule)" fill="none"/></svg>
  <div class="footer-band"></div>
</section>

<section class="sheet invoice">
  <div class="brand"><span class="dot"></span>Bright Path</div>
  <div class="title">INVOICE</div>
  <div class="meta"><div class="field">Invoice #</div><div class="field">Date:</div></div>
  <div class="bill"><div class="field">Bill To:</div><div class="field">Address:</div></div>
  <table>
    <thead><tr><th>Qty</th><th>Description</th><th>Price</th><th>Amount</th></tr></thead>
    <tbody><tr><td></td><td></td><td></td><td></td></tr><tr><td></td><td></td><td></td><td></td></tr><tr><td></td><td></td><td></td><td></td></tr><tr><td></td><td></td><td></td><td></td></tr><tr><td></td><td></td><td></td><td></td></tr><tr><td></td><td></td><td></td><td></td></tr><tr><td></td><td></td><td></td><td></td></tr><tr><td></td><td></td><td></td><td></td></tr><tr><td></td><td></td><td></td><td></td></tr><tr><td></td><td></td><td></td><td></td></tr><tr><td></td><td></td><td></td><td></td></tr></tbody>
  </table>
  <div class="total"><div class="field">Subtotal</div><div class="field">Total</div></div>
  <div class="footer-band"></div>
</section>

<section class="sheet card front" style="left:463px;top:408px">
  <div class="brand"><span class="dot"></span>Bright Path</div>
  <div class="info"><b>Monica Lindqvist</b><br>Physical Therapist<br>27415 PT Hargrove Blvd # D<br>Palo Mesa North, AZ 85291<br>www.brightpathrehab.com</div>
  <div class="footer-band"></div>
</section>
<section class="sheet card back" style="left:463px;top:504px">
  <div class="brand light"><span class="dot"></span>Bright Path</div>
  <div class="tag">Comprehensive Outpatient Rehabilitation Facility</div>
  <div class="footer-band dark"></div>
</section>

<section class="sheet referral">
  <div class="brand"><span class="dot"></span>Bright Path</div>
  <div class="title">Physical Therapy<br>Referral</div>
  <div class="fields">
    <div class="field">Patient Name:</div>
    <div class="field">Date of Birth:</div>
    <div class="field">Diagnosis:</div>
    <div class="field">Frequency / Duration:</div>
  </div>
  <div class="rx">Rx</div>
  <div class="map" role="img" aria-label="Street map showing the clinic location"></div>
  <div class="sign"><div class="field">Physician</div><div class="field">Signature</div></div>
  <div class="footer-band"></div>
</section>

<div class="lockup">
  <div class="brand"><span class="dot"></span>Bright Path Rehabilitation</div>
</div>

</body>
</html>
```